Veltora Software Business Card Design

We are a new organization called Veltora. We are a software as a service provider. We deliver a project and program management solution via the internet, so everyone has the ability to work together and collaborate. Its an enterprise platform and we will focus on 50 plus employee company.

We have a website in place
www.veltora-demo.com

Use this as a start of producing the business card. The logo is there as well, but if you have a great and better solution...

Color scheme's could be inline with the website, but don't pin point on it. We can always change the website, logo, color scheme etc.

Target Market(s)

B2B, Projectmembers, projectmanagers, ICT, CTO, Marketing Managers

Industry/Entity Type

Software

Requirements
Must have
• Marten Kuyvelsma

Tel: +31 255 47 09 36
Mob: +31 6 927 15 062
marten@veltora-demo.com
Oostelingpad 84c
2184 KT Zuidwervel

Www.veltora-demo.com
social media links

```html
<!DOCTYPE html>
<html lang="en">
<head>
<meta charset="utf-8">
<title>Veltora Business Card</title>
<link rel="stylesheet" href="https://fonts.googleapis.com/css2?family=Arimo:wght@400;700&family=Roboto:wght@300&display=swap">
<style>
  :root {
    --stage: #3a3a3a;
    --card-white: #ffffff;
    --orange: #e8552a;
    --orange-light: #f07a3a;
    --blue: #1a6fc0;
    --ink: #2b2b2b;
    --white: #ffffff;
  }
  * { margin: 0; padding: 0; box-sizing: border-box; }
  html, body { width: 1200px; height: 900px; overflow: hidden; }
  body {
    background: var(--stage);
    font-family: "Arimo", Arial, sans-serif;
    position: relative;
  }
  .card {
    position: absolute;
    left: 300px;
    width: 600px;
    height: 340px;
    box-shadow: 0 10px 30px rgba(0,0,0,0.45);
  }

  /* Front */
  .card-front { top: 90px; background: var(--card-white); }
  .front-logo {
    position: absolute; left: 34px; top: 34px;
    font-family: "Roboto", Arial, sans-serif; font-weight: 300;
    font-size: 48px; color: var(--orange); letter-spacing: 0.5px;
  }
  .holder { position: absolute; top: 112px; left: 0; right: 0; text-align: center; }
  .holder-name { font-weight: 700; font-size: 24px; color: var(--blue); }
  .holder-role { font-size: 12px; color: var(--ink); margin-top: 3px; }
  .details {
    position: absolute; left: 34px; right: 30px; bottom: 44px;
    display: flex; align-items: flex-end; justify-content: space-between;
    font-size: 12.5px; line-height: 1.45; color: var(--ink);
    letter-spacing: 0.3px; white-space: nowrap;
  }
  .detail-col { padding-left: 12px; border-left: 2px solid var(--orange); }
  .detail-col.address { border-left: none; padding-left: 0; }
  .label { color: var(--orange); }
  .front-band {
    position: absolute; left: 0; right: 0; bottom: 0; height: 26px;
    background: var(--orange);
  }

  /* Back */
  .card-back { top: 470px; background: var(--orange); }
  .back-mark {
    position: absolute; left: 50%; top: 50px; transform: translateX(-50%);
    display: flex; flex-direction: column; align-items: center; gap: 10px;
  }
  .mark-square { width: 86px; height: 86px; border-radius: 6px; background: var(--orange-light); }
  .mark-name { font-size: 20px; color: var(--white); }
  .back-url {
    position: absolute; top: 212px; left: 0; right: 0; text-align: center;
    color: var(--white); font-size: 19px; letter-spacing: 6px;
  }
  .back-social {
    position: absolute; bottom: 34px; left: 0; right: 0;
    display: flex; justify-content: center; gap: 18px;
    color: var(--white); font-size: 14px;
  }
  .social-item { display: flex; align-items: center; gap: 5px; padding-right: 18px; border-right: 1px solid rgba(255,255,255,0.7); }
  .social-item:last-child { border-right: none; padding-right: 0; }
  .social-dot { width: 12px; height: 12px; background: var(--white); opacity: 0.85; }
</style>
</head>
<body>
  <section class="card card-front">
    <div class="front-logo">Veltora</div>
    <div class="holder">
      <div class="holder-name">Marten Kuyvelsma</div>
      <div class="holder-role">Director</div>
    </div>
    <div class="details">
      <div class="detail-col address">
        <div class="label">Address:</div>
        <div>Oostelingpad 84c</div>
        <div>2184 KT Zuidwervel</div>
      </div>
      <div class="detail-col contact">
        <div><span class="label">Tel:</span> +31 255 47 09 36</div>
        <div><span class="label">Mob:</span> +31 6 927 15 062</div>
        <div><span class="label">Mail:</span> marten@veltora-demo.com</div>
      </div>
      <div class="detail-col social">
        <div><span class="label">Facebook:</span> @Veltora</div>
        <div><span class="label">Twister:</span> @VeltoraCOM</div>
        <div><span class="label">Linkedin:</span> @Veltora</div>
      </div>
    </div>
    <div class="front-band"></div>
  </section>

  <section class="card card-back">
    <div class="back-mark">
      <div class="mark-square"></div>
      <div class="mark-name">Veltora</div>
    </div>
    <div class="back-url">www.veltora-demo.com</div>
    <div class="back-social">
      <div class="social-item"><span class="social-dot"></span>@VeltoraCOM</div>
      <div class="social-item"><span class="social-dot"></span>@Veltora</div>
      <div class="social-item"><span class="social-dot"></span>@Veltora</div>
    </div>
  </section>
</body>
</html>
```